Flyer for the Lumen 2025 Conference

I am looking to produce a flyer for our upcoming conference, Lumen 2025. This is an annual conference that we plan to publicize on social media. The ideal designer will create a flyer that is eye-catching and effectively communicates the key information. Please see attached our logo, speaker photo, and flyer content.

Target Market(s)

All demographics

Industry/Entity Type

Christian

Font styles to use
Sans Serif

Requirements
Should not have
• Cross, church

```html
<!DOCTYPE html>
<html lang="en">
<head>
<meta charset="utf-8">
<title>Lumen 2025 – A Prophetic Conference</title>
<link rel="stylesheet" href="https://fonts.googleapis.com/css2?family=Inter:wght@300;400;500;700;800&display=swap">
<style>
  :root {
    --ink: #0b0b0c;
    --white: #ffffff;
    --orange: #f7931e;
    --gold: #f5b21b;
    --glow: #e0720f;
    --suit: #13416f;
    --panel: rgba(120, 70, 20, 0.55);
    --panel-dark: rgba(10, 10, 12, 0.78);
  }
  * { margin: 0; padding: 0; box-sizing: border-box; }
  html, body { width: 894px; height: 1200px; overflow: hidden; background: var(--ink); }
  .flyer {
    position: relative; width: 894px; height: 1200px; overflow: hidden;
    background: var(--ink); color: var(--white);
    font-family: "Inter", Arial, sans-serif;
  }
  .speaker-photo {
    position: absolute; inset: 0;
    background:
      radial-gradient(circle at 447px 500px, rgba(0,0,0,0) 0 240px, rgba(230,120,20,0.85) 262px, rgba(150,60,5,0.45) 300px, rgba(0,0,0,0) 340px),
      radial-gradient(ellipse 260px 520px at 330px 780px, rgba(19,65,111,0.95), rgba(19,65,111,0) 100%),
      radial-gradient(circle at 447px 500px, #3a1a06 0, #120904 300px, var(--ink) 420px);
  }
  .headline {
    position: absolute; left: 53px; top: 128px;
    font-size: 66px; line-height: 75px; font-weight: 700; letter-spacing: -0.5px;
  }
  .brand {
    position: absolute; left: 640px; top: 70px;
    display: flex; align-items: center; gap: 10px;
  }
  .brand-dot { width: 22px; height: 22px; border-radius: 50%; background: var(--orange); }
  .brand-name { font-size: 40px; font-weight: 500; color: var(--orange); letter-spacing: 1px; }
  .info-label {
    position: absolute; left: 581px; font-size: 20px; font-weight: 300;
  }
  .speaker-box {
    position: absolute; left: 567px; top: 370px; width: 295px; height: 49px;
    border: 1px solid rgba(245,178,27,0.7); border-radius: 9px; background: var(--panel);
    display: flex; align-items: center; padding-left: 20px;
    font-size: 23px; font-weight: 700;
  }
  .schedule {
    position: absolute; left: 567px; top: 492px; width: 295px; height: 107px;
    border: 1.5px solid var(--gold); border-radius: 9px; background: var(--panel-dark);
    list-style: none; display: flex; flex-direction: column;
  }
  .schedule li {
    flex: 1; display: flex; align-items: center; padding-left: 20px;
    font-size: 11.5px; font-weight: 700;
  }
  .schedule li + li { border-top: 1px solid var(--gold); }
  .venue-box {
    position: absolute; left: 567px; top: 674px; width: 295px; height: 70px;
    border: 1px solid var(--gold); border-radius: 9px; background: var(--panel-dark);
    padding: 15px 20px 0; font-size: 11.5px; font-weight: 700; line-height: 14px;
  }
  .event-title {
    position: absolute; left: 0; right: 0; top: 900px; text-align: center;
    font-size: 118px; font-weight: 800; color: var(--orange); letter-spacing: 1px; line-height: 1;
  }
  .event-subtitle {
    position: absolute; left: 0; right: 0; top: 1030px; text-align: center;
    font-size: 42px; font-weight: 300;
  }
  .app-pill {
    position: absolute; left: 33px; top: 1134px; width: 422px; height: 39px;
    border: 1px solid rgba(255,255,255,0.35); border-radius: 10px;
    display: flex; align-items: center; padding-left: 18px;
    font-size: 12.5px; font-weight: 400; letter-spacing: 0.2px;
  }
  .contacts {
    position: absolute; right: 32px; top: 1144px;
    display: flex; align-items: center; font-size: 12.5px; font-weight: 400;
  }
  .contacts span + span { border-left: 1px solid rgba(255,255,255,0.8); margin-left: 12px; padding-left: 14px; }
</style>
</head>
<body>
<main class="flyer">
  <div class="speaker-photo" role="img" aria-label="Portrait of the speaker in a blue suit and grey turtleneck, seated before a glowing orange ring of light"></div>

  <h1 class="headline">The<br>Voice Of<br>The Lord</h1>

  <div class="brand"><span class="brand-dot"></span><span class="brand-name">KAVORA</span></div>

  <p class="info-label" style="top:330px">Speaker:</p>
  <div class="speaker-box">Prophet Elias Marundu</div>

  <p class="info-label" style="top:452px">Date/Time:</p>
  <ul class="schedule">
    <li>Friday, December 26th, 6:30PM - 9:00PM</li>
    <li>Saturday, December 27th, 5:30PM &nbsp;- 8:00PM</li>
    <li>Sunday, December 29th, 4:30PM - 7:00PM</li>
  </ul>

  <p class="info-label" style="top:629px">Location:</p>
  <address class="venue-box" style="font-style:normal">
    The Harlow Performing Arts Center<br>
    218 Brookfield Avenue Eastmoor,<br>
    Vermont 05120
  </address>

  <h2 class="event-title">LUMEN 2025</h2>
  <p class="event-subtitle">A Prophetic Conference</p>

  <div class="app-pill">DOWNLOAD THE KAVORA APP TO STAY UPDATED ON THE EVENT</div>
  <div class="contacts">
    <span>802 555 0147</span>
    <span>contact@kavora.org</span>
    <span>www.kavora.org</span>
  </div>
</main>
</body>
</html>
```